Start up in business consultancy needs a business card

We need the business card's layout (we have already the logo). Our business is concerned on consultancy services delivered to companies on the matter of sustainability. Business card should be enough essentials and professional style.

Side A with the following info:
logo + a space for the claim (still to identify) + website of the company

Side B with the following info:
Name of business card holder + title of the business card holder + address of the company + space for mobile number, phone number, fax number + e-mail of business card holder + graphic details around.

Target Market(s)

Business of any sector

Industry/Entity Type

Business Service

Contact Information for Business Card

Name of the company:
Pianoverde srl
Società Benefit

Address of the company:
Via Lucerna, 7
21047 - Saronno (VA)

Website:
www.pianoverde.it

Name of the BC' holder:
Luca Ferentino

Title:
Co-fondatore

Email:
luca@pianoverde.it

Mobile:
+39 348 915 2074
Phone:
+39 348 915 2074
Fax:
+39 348 915 2074

Font styles to use
Other font styles liked:
• new gothic

```html
<!DOCTYPE html>
<html lang="it">
<head>
<meta charset="utf-8">
<title>Pianoverde – Biglietto da visita</title>
<link rel="stylesheet" href="https://fonts.googleapis.com/css2?family=Lato:wght@400;700;900&display=swap">
<style>
  :root {
    --bg: #3a3a3a;
    --card-white: #ffffff;
    --brand-blue: #0a64a8;
    --brand-blue-light: #3f87c3;
    --back-blue: #0766a8;
    --on-blue: #ffffff;
  }
  * { margin: 0; padding: 0; box-sizing: border-box; }
  html, body {
    width: 900px; height: 1200px; overflow: hidden;
    background: var(--bg);
    font-family: "Lato", sans-serif;
  }
  .canvas { position: relative; width: 900px; height: 1200px; }
  .card {
    position: absolute; left: 117px; width: 673px; height: 395px;
    border-radius: 22px; overflow: hidden;
  }
  .card--front { top: 175px; background: var(--card-white); color: var(--brand-blue); }
  .card--back { top: 630px; background: var(--back-blue); color: var(--on-blue); }

  .brand { position: absolute; display: flex; align-items: center; }
  .brand__dot { border-radius: 50%; flex: none; }
  .brand__name { font-weight: 700; line-height: 1; letter-spacing: -0.5px; }

  .card--front .brand { left: 120px; top: 77px; gap: 20px; }
  .card--front .brand__dot { width: 130px; height: 130px; border: 6px solid var(--brand-blue); }
  .card--front .brand__name { font-size: 46px; color: var(--brand-blue); }

  .holder { position: absolute; left: 44px; top: 273px; }
  .holder__name { font-size: 20px; font-weight: 700; letter-spacing: 0.2px; text-transform: uppercase; }
  .holder__title { font-size: 15px; color: var(--brand-blue-light); margin-top: 3px; }
  .address { position: absolute; right: 38px; top: 296px; font-size: 15px; }
  .divider { position: absolute; left: 44px; right: 38px; top: 320px; height: 2px; background: var(--brand-blue); }

  .contacts { position: absolute; left: 44px; top: 329px; font-size: 15px; line-height: 22px; }
  .contacts__row { display: flex; align-items: center; gap: 10px; }
  .contact { display: inline-flex; align-items: center; gap: 5px; }
  .contact svg { width: 13px; height: 13px; fill: var(--brand-blue); }

  .watermark-ring {
    position: absolute; left: 378px; top: 12px; width: 330px; height: 330px;
    border-radius: 50%; border: 6px solid rgba(255,255,255,0.14);
  }
  .card--back .brand { left: 46px; top: 276px; gap: 14px; }
  .card--back .brand__dot { width: 84px; height: 84px; border: 4px solid var(--on-blue); }
  .card--back .brand__name { font-size: 30px; color: var(--on-blue); }
  .website { position: absolute; left: 144px; top: 333px; font-size: 15px; font-weight: 700; }
</style>
</head>
<body>
<main class="canvas">
  <section class="card card--front" aria-label="Fronte del biglietto">
    <div class="brand">
      <span class="brand__dot"></span>
      <span class="brand__name">pianoverde</span>
    </div>

    <div class="holder">
      <p class="holder__name">Luca Ferentino</p>
      <p class="holder__title">Co-fondatore</p>
    </div>
    <p class="address">Via Lucerna, 7 , 21047 - Saronno (VA)</p>
    <div class="divider"></div>

    <div class="contacts">
      <div class="contacts__row">
        <span class="contact">
          <svg viewBox="0 0 16 16" aria-label="Cellulare"><path d="M4 1h8a1 1 0 0 1 1 1v12a1 1 0 0 1-1 1H4a1 1 0 0 1-1-1V2a1 1 0 0 1 1-1zm1 2v9h6V3z"/></svg>
          +39 348 915 2074
        </span>
        <span class="contact">
          <svg viewBox="0 0 16 16" aria-label="Telefono"><path d="M3.6 1.5l2.2 2.6-1.2 1.8c.9 2 2.6 3.7 4.5 4.6l1.8-1.2 2.6 2.2-1.4 2.5C6.8 13.6 2.4 9.2 1.1 3z"/></svg>
          +39 348 915 2074
        </span>
        <span class="contact">
          <svg viewBox="0 0 16 16" aria-label="Fax"><path d="M4 1h7v4H4zM1 6h14v6h-3v3H4v-3H1zm4 5v3h6v-3z"/></svg>
          +39 348 915 2074
        </span>
      </div>
      <div class="contacts__row">
        <span class="contact">
          <svg viewBox="0 0 16 16" aria-label="Email"><path d="M1 3h14v10H1zm1.5 1.5L8 9l5.5-4.5z"/></svg>
          luca@pianoverde.it
        </span>
      </div>
    </div>
  </section>

  <section class="card card--back" aria-label="Retro del biglietto">
    <div class="watermark-ring"></div>
    <div class="brand">
      <span class="brand__dot"></span>
      <span class="brand__name">pianoverde</span>
    </div>
    <p class="website">www.pianoverde.it</p>
  </section>
</main>
</body>
</html>
```